Basketball Training Facility Flyer Design

We need a killer flyer designed for our brand new state of the art basketball training facility here in Syracuse, Utah. This flyer will be distributed to coaches, parents and players in a large school district in Davis and Weber county, Utah. The purpose of the flyer is to announce the launch of the new facility and to encourage parents, coaches and players to come and try out the facility for a free initial session. We're offering a completely complimentary first training session to introduce customers to the facility at no cost.

We use technology and equipment that is typically found in PLH-level training facilities and gymnasiums. Our website can be found here for some additional information - www.corvanhoopworks.com. Customers can easily book and pay online through our website (the functionality will be done by the time we distribute the completed flyer).

The design needs to highlight the equipment we offer at the facility, because no other basketball training center has the same level of technology we do. We want the flyer to be clean and simple.

Please see must haves for specific details.

The size of the flyer we want to print is 5.75 inches by 9.5 inches.

Target Market(s)

Parents of basketball players of all skill levels age 8-18.

Industry/Entity Type

Training

Requirements
Must have
• Design must include this header: You want to dominate on the court. We have the formula to make that happen.

Design must include this sub header or highlight: Free Introductory Training Session!

The design must include our Logo

The design must include the photos attached of the Rebo, the Jumplora and the Dribtek

Under the the photo of the Rebo 4200 (attached) please include this verbiage:
Game Shots in Game Spots at Game Speed

Under the photo of the Jumplora (see attached) please include this verbiage:
Improve Power, Agility and Speed like Never Before

Under the photo of the Dribtek (attached) please include this verbiage:
Real Time Statistics to Improve Dribble Speed, Accuracy and Right / Left Comparison

Include this verbiage somewhere in the design: Technology Used by PLH and the Best D-1 College Teams

The design must include a strong call to action: Call or Click Now to Schedule A Free Training Session!

The design must include our contact information in easy-to-read font and size (also specifically highlighting the website):

Schedule Online in Less Than 60 Seconds!
Call or Click
801-482-7195
www.corvanhoopworks.com
Nice to have
• For examples of the type of design we like, please see the attached images labeled

Please use stock photos of your preference to go in the flyer (preferably images of youth basketball training or kids in basketball training)

We don't want the flyer to be too cluttered, so please use images at your discretion.

Thank you!

```html
<!DOCTYPE html>
<html lang="en">
<head>
<meta charset="utf-8">
<title>Corvan Hoopworks – Free Introductory Training Session</title>
<link rel="stylesheet" href="https://fonts.googleapis.com/css2?family=Orbitron:wght@700;900&family=Russo+One&family=Oswald:wght@600&family=Open+Sans:ital,wght@0,700;1,700&display=swap">
<style>
  :root {
    --black: #050505;
    --orange: #ff4a12;
    --orange-text: #f2561d;
    --red-deep: #c81a0c;
    --red-hot: #ff3b12;
    --glow: #ffb21a;
    --silver-light: #ffffff;
    --silver-mid: #c9c9c9;
    --silver-dark: #8a8a8a;
    --panel: #f1f1f1;
    --ink: #111111;
    --white: #ffffff;
  }
  * { margin: 0; padding: 0; box-sizing: border-box; }
  html, body { width: 900px; height: 1200px; overflow: hidden; background: var(--white); }
  .canvas { position: relative; width: 900px; height: 1200px; }

  .flyer {
    position: absolute; left: 88px; top: 25px; width: 702px; height: 1147px;
    background: var(--black);
    box-shadow: 10px 12px 10px rgba(0,0,0,0.45);
    overflow: hidden;
  }

  .hero-band {
    position: absolute; left: 0; top: 220px; width: 702px; height: 350px;
    background: radial-gradient(ellipse 55% 60% at 52% 48%, var(--glow) 0%, var(--red-hot) 45%, var(--red-deep) 100%);
  }
  .player-photo {
    position: absolute; left: 252px; top: 65px; width: 325px; height: 510px;
    background: linear-gradient(170deg, #3a2a22 0%, #1a1a1a 45%, #b3231a 75%, #2a1a14 100%);
    border-radius: 40% 40% 30% 30% / 20% 20% 20% 20%;
    opacity: 0.9;
  }

  .headline-lead {
    position: absolute; left: 0; top: 14px; width: 702px; text-align: center;
    font-family: "Orbitron", sans-serif; font-weight: 900; font-size: 42px;
    color: var(--orange); letter-spacing: 1px;
  }
  .headline-main {
    position: absolute; left: 0; top: 68px; width: 702px; text-align: center;
    font-family: "Russo One", sans-serif; font-size: 122px; line-height: 1;
    letter-spacing: 2px;
    background: linear-gradient(180deg, var(--silver-light) 0%, var(--silver-mid) 48%, var(--silver-dark) 52%, var(--silver-light) 100%);
    -webkit-background-clip: text; background-clip: text; color: transparent;
  }
  .headline-tail {
    position: absolute; left: 0; top: 168px; width: 702px; text-align: center;
    font-family: "Orbitron", sans-serif; font-weight: 900; font-size: 50px;
    color: var(--orange); letter-spacing: 2px;
  }

  .formula {
    position: absolute; left: 8px; top: 318px;
    font-family: "Russo One", sans-serif; font-size: 38px; line-height: 1.08;
    text-transform: uppercase;
  }
  .formula .muted { color: var(--silver-mid); }
  .formula .bright { color: var(--white); }

  .offer-strip {
    position: absolute; left: 0; top: 572px; width: 702px; height: 36px;
    background: var(--black); text-align: center;
    font-family: "Orbitron", sans-serif; font-weight: 900; font-size: 27px;
    color: var(--orange); line-height: 36px; letter-spacing: 0.5px;
  }

  .tech-panel {
    position: absolute; left: 0; top: 608px; width: 702px; height: 277px;
    background: linear-gradient(135deg, #ffffff 0%, var(--panel) 50%, #dcdcdc 100%);
  }
  .tech-title {
    position: absolute; left: 0; top: 4px; width: 702px; text-align: center;
    font-family: "Oswald", sans-serif; font-weight: 600; font-size: 26px;
    color: var(--ink); transform: scaleX(0.92);
  }
  .product { position: absolute; text-align: center; }
  .product-photo { margin: 0 auto; }
  .product-caption {
    font-family: "Orbitron", sans-serif; font-weight: 700; font-size: 14px;
    line-height: 1.05; color: var(--ink); text-transform: uppercase;
  }
  .product--rebo { left: 10px; top: 42px; width: 160px; }
  .product--rebo .product-photo { width: 125px; height: 165px;
    background: linear-gradient(180deg, #e8e8e8 0%, #d23a2a 55%, #9a2418 100%); border-radius: 6px; }
  .product--rebo .product-caption { margin-top: 12px; }
  .product--jumplora { left: 205px; top: 38px; width: 220px; }
  .product--jumplora .product-photo { width: 165px; height: 158px;
    background: linear-gradient(160deg, #2f5ec8 0%, #8ea0c0 55%, #c9a336 100%); border-radius: 8px; }
  .product--jumplora .product-caption { margin-top: 6px; }
  .product--dribtek { left: 440px; top: 42px; width: 250px; }
  .product--dribtek .product-photo { width: 120px; height: 130px;
    background: radial-gradient(circle at 40% 40%, #e58a3c 0%, #b6541e 60%, #3a2a22 100%); border-radius: 50%; }
  .product--dribtek .product-caption { margin-top: 22px; font-size: 13px; }

  .credentials {
    position: absolute; left: 0; top: 893px; width: 702px; text-align: center;
    font-family: "Orbitron", sans-serif; font-weight: 900; font-size: 18.5px;
    color: var(--orange);
  }
  .services {
    position: absolute; left: 9px; top: 918px; list-style: none;
    font-family: "Open Sans", sans-serif; font-weight: 700; font-size: 19px;
    line-height: 28.5px; color: var(--white);
  }
  .services .highlight { color: var(--orange-text); }
  .services .note { font-style: italic; color: var(--white); }

  .schedule {
    position: absolute; left: 0; top: 1036px; width: 702px; text-align: center;
    font-family: "Orbitron", sans-serif; font-weight: 900; font-size: 23.5px;
    color: var(--orange);
  }

  .brand {
    position: absolute; left: 18px; top: 1088px; display: flex; align-items: center; gap: 14px;
  }
  .brand-mark { width: 50px; height: 50px; border-radius: 50%; background: var(--orange); }
  .brand-name {
    font-family: "Orbitron", sans-serif; font-weight: 900; font-size: 19px; color: var(--white);
    text-transform: uppercase;
  }

  .contact {
    position: absolute; right: 18px; top: 1068px; text-align: right;
    font-family: "Open Sans", sans-serif; font-weight: 700; line-height: 1.2;
  }
  .contact-cta { font-size: 21px; color: var(--orange-text); }
  .contact-phone { font-size: 18px; color: var(--white); }
  .contact-web { font-size: 20px; color: var(--white); }
</style>
</head>
<body>
<div class="canvas">
  <main class="flyer">
    <div class="hero-band"></div>
    <div class="player-photo" role="img" aria-label="Photo of a basketball player mid-air going up for a dunk, wearing black jersey and red shorts"></div>

    <h1>
      <span class="headline-lead">YOU WANT TO</span>
      <span class="headline-main">DOMINATE</span>
      <span class="headline-tail">ON THE COURT?</span>
    </h1>

    <p class="formula">
      <span class="muted">We have the<br>formula to</span><br>
      <span class="bright">make that<br>happen.</span>
    </p>

    <h2 class="offer-strip">FREE INTRODUCTORY TRAINING SESSION!</h2>

    <section class="tech-panel">
      <h3 class="tech-title">FIND OUT WHY SUPERIOR TECHNOLOGY = SUPERIOR TRAINING</h3>

      <figure class="product product--rebo">
        <div class="product-photo" role="img" aria-label="Photo of the Rebo 4200 shooting machine with return net"></div>
        <figcaption class="product-caption">Game shots in<br>game spots at<br>game speed</figcaption>
      </figure>

      <figure class="product product--jumplora">
        <div class="product-photo" role="img" aria-label="Photo of an athlete training on the Jumplora resistance platform"></div>
        <figcaption class="product-caption">Improve power, agility<br>and speed like never<br>before</figcaption>
      </figure>

      <figure class="product product--dribtek">
        <div class="product-photo" role="img" aria-label="Photo of the Dribtek sensor basketball beside a smartphone showing stats"></div>
        <figcaption class="product-caption">Basketball sensors with<br>real time statistics to<br>improve dribble speed,<br>accuracy and right / left<br>comparison</figcaption>
      </figure>
    </section>

    <p class="credentials">TECHNOLOGY USED BY PLH AND THE BEST D-1 COLLEGE TEAMS</p>

    <ul class="services">
      <li>One on One / Individual Sessions</li>
      <li><span class="highlight">Group Sessions</span> <span class="note">(2-5 players with discounts applying)</span></li>
      <li>Team Training</li>
      <li>Monthly Memberships</li>
    </ul>

    <p class="schedule">SCHEDULE ONLINE IN LESS THAN 60 SECONDS!</p>

    <div class="brand">
      <span class="brand-mark"></span>
      <span class="brand-name">Corvan Hoopworks</span>
    </div>

    <address class="contact">
      <div class="contact-cta">Call or Click</div>
      <div class="contact-phone">801-482-7195</div>
      <div class="contact-web">www.corvanhoopworks.com</div>
    </address>
  </main>
</div>
</body>
</html>
```